Hula-Hoop dance entertainment sales and instruction by spin-wisp needs a business card

I need a 2 sided business card that is square (although this is not an absolute )for my self employed business as an independent artist. my business name is "Spin-Wisp" I teach how to hula-hoop classes, make and sell hula-hoops, provided entertainment at kids birthday parties, community events, corporate events and perform at artistic dance shows.
I would like to see spirals or curved lines in the card, and I would like the card to be seen as fun, spunky, flair and eye catching.

the card could double as a tag to go on the hoops i sell,

Target Market(s)

women age 20 - 50

Industry/Entity Type

Entertainment

Requirements
Must have
• Dena Marwick
www.spinwispdemo.com
555.014.7263
Nice to have
• I would like my image to be on one side of the card. so people can recognize me!

```html
<!DOCTYPE html>
<html lang="en">
<head>
<meta charset="utf-8">
<title>Spin-Wisp Business Card</title>
<link rel="stylesheet" href="https://fonts.googleapis.com/css2?family=Princess+Sofia&family=Quicksand:wght@500&family=Roboto+Condensed:wght@400&display=swap">
<style>
  :root {
    --stripe-dark: #1a6fb5;
    --stripe-light: #4fd7fa;
    --name-pink: #e621d4;
    --title-blue: #1570b0;
    --copy-blue: #2b2fd6;
    --paper: #ffffff;
    --shadow: rgba(0, 0, 0, 0.45);
  }
  html, body {
    margin: 0;
    padding: 0;
    width: 1200px;
    height: 1000px;
    overflow: hidden;
    background: var(--paper);
  }
  .canvas {
    position: relative;
    width: 1200px;
    height: 1000px;
  }
  .card {
    position: absolute;
    width: 592px;
    height: 592px;
    overflow: hidden;
    box-shadow: 5px 5px 5px var(--shadow);
  }
  .card-front {
    left: 50px;
    top: 32px;
    background: repeating-linear-gradient(
      45deg,
      var(--stripe-light) 0 44px,
      var(--stripe-dark) 44px 88px
    );
  }
  .front-oval {
    position: absolute;
    inset: 0;
  }
  .holder-name {
    position: absolute;
    right: 62px;
    top: 158px;
    margin: 0;
    font-family: "Princess Sofia", cursive;
    font-weight: 400;
    font-size: 60px;
    color: var(--name-pink);
    letter-spacing: 1px;
    white-space: nowrap;
  }
  .holder-title {
    position: absolute;
    right: 64px;
    top: 228px;
    margin: 0;
    font-family: "Quicksand", sans-serif;
    font-weight: 500;
    font-size: 21px;
    color: var(--title-blue);
  }
  .holder-web {
    position: absolute;
    left: 59px;
    top: 388px;
    margin: 0;
    font-family: "Quicksand", sans-serif;
    font-weight: 500;
    font-size: 20px;
    color: var(--title-blue);
  }
  .holder-phone {
    position: absolute;
    left: 57px;
    top: 424px;
    margin: 0;
    font-family: "Princess Sofia", cursive;
    font-size: 40px;
    color: var(--name-pink);
    letter-spacing: 1px;
  }
  .card-back {
    left: 568px;
    top: 360px;
  }
  .back-photo {
    position: absolute;
    inset: 0;
    background:
      radial-gradient(ellipse 60% 40% at 55% 40%, #f04a8a 0%, rgba(240,74,138,0) 70%),
      radial-gradient(ellipse 40% 45% at 60% 85%, #c9b7a8 0%, rgba(201,183,168,0) 70%),
      linear-gradient(160deg, #d8304a 0%, #e8602a 35%, #f08a2c 65%, #c64a20 100%);
  }
  .services-oval {
    position: absolute;
    left: 150px;
    top: 118px;
    width: 382px;
    height: 190px;
    border-radius: 50%;
    background: rgba(255, 240, 225, 0.82);
  }
  .services-copy {
    position: absolute;
    left: 130px;
    top: 138px;
    width: 420px;
    margin: 0;
    text-align: center;
    font-family: "Roboto Condensed", sans-serif;
    font-size: 19.5px;
    line-height: 29px;
    color: var(--copy-blue);
  }
</style>
</head>
<body>
<div class="canvas">
  <section class="card card-front">
    <svg class="front-oval" width="592" height="592" viewBox="0 0 592 592" aria-hidden="true">
      <ellipse cx="312" cy="310" rx="360" ry="250" transform="rotate(-24 312 310)" fill="#ffffff"/>
    </svg>
    <h1 class="holder-name">Dena Marwick</h1>
    <p class="holder-title">Spin-Wisp</p>
    <p class="holder-web">www.spinwispdemo.com</p>
    <p class="holder-phone">555.014.7263</p>
  </section>

  <section class="card card-back">
    <div class="back-photo" role="img" aria-label="Photo of the performer holding a hoop, surrounded by a spiral of colourful taped hula-hoops on a wooden floor"></div>
    <div class="services-oval"></div>
    <p class="services-copy">Teach hula-hoop classes,<br>make and sell hula-hoops, provided<br>entertainment at kids birthday parties,<br>community events, corporate events and<br>perform at artistic dance shows.</p>
  </section>
</div>
</body>
</html>
```